New Web Design Project

New Roofing Website homepage mockup

Complete design document here: https://files.plorvex.net/doc/7tQmZrA2kLwP9xVbN4cYhE3sJdF8gUoR6iKe1nTy/edit?usp=sharing
Updates

Number of Pages Required

1 page

Font styles to use
Sans Serif

```html
<!DOCTYPE html>
<html lang="en">
<head>
<meta charset="utf-8">
<title>Evergreen Roofing — Built Right, Built to Last</title>
<link href="https://fonts.googleapis.com/css2?family=Montserrat:wght@400;500;600;700&family=Open+Sans:wght@400;600&display=swap" rel="stylesheet">
<style>
:root{
  --blue:#29a3e0;
  --blue-deep:#1d6b9c;
  --ink:#222a33;
  --text:#555;
  --muted:#8a8f96;
  --grey-band:#f2f2f2;
  --navy:#1b2632;
  --footer:#1b1f24;
  --white:#fff;
}
*{box-sizing:border-box;margin:0;padding:0}
html,body{width:1200px;height:4279px;overflow:hidden}
body{position:relative;background:var(--white);font-family:"Open Sans",Arial,sans-serif;color:var(--text)}
.abs{position:absolute}
.head-font{font-family:"Montserrat",Arial,sans-serif}
.btn{position:absolute;background:var(--blue);color:var(--white);font:700 11px "Montserrat",Arial,sans-serif;display:flex;align-items:center;justify-content:center;letter-spacing:.3px}

/* header */
.site-header{position:absolute;left:0;top:0;width:1200px;height:77px;background:var(--white)}
.brand{position:absolute;left:93px;top:26px;display:flex;align-items:center;gap:8px;font:700 20px "Montserrat",Arial,sans-serif;color:var(--blue)}
.brand-mark{width:16px;height:16px;background:var(--blue)}
.call{position:absolute;right:93px;top:12px;font:400 12px "Montserrat",sans-serif;color:var(--ink)}
.call b{color:var(--blue);font-weight:600}
.nav{position:absolute;right:93px;top:52px;display:flex;gap:36px;font:500 12px "Montserrat",sans-serif;color:var(--ink)}
.nav .active{color:var(--blue)}

/* hero */
.hero{position:absolute;left:0;top:77px;width:1200px;height:523px;background:linear-gradient(180deg,#5b6670 0%,#3f4a52 50%,#33403a 100%)}
.hero-kicker{position:absolute;left:0;width:1200px;top:180px;text-align:center;font:500 33px "Montserrat",sans-serif;color:var(--white)}
.hero-title{position:absolute;left:0;width:1200px;top:218px;text-align:center;font:700 63px "Montserrat",sans-serif;color:var(--white)}
.hero .btn{left:515px;top:300px;width:170px;height:35px}
.dots{position:absolute;left:1076px;top:491px;display:flex;gap:4px}
.dots i{width:8px;height:8px;background:var(--white)}
.dots i:first-child{background:var(--blue)}

/* services */
.sec-kicker{font:500 22px "Montserrat",sans-serif;color:var(--ink)}
.sec-title{font:700 42px "Montserrat",sans-serif;color:var(--ink);line-height:1}
.services-intro{position:absolute;left:93px;top:703px;width:320px}
.services-intro p{margin-top:20px;font-size:12px;line-height:21px;color:var(--text)}
.service-card{position:absolute;top:653px;width:328px}
.service-card .photo{height:258px}
.service-card h3{margin-top:14px;font:500 21px "Montserrat",sans-serif;color:var(--ink)}
.service-card p{margin-top:10px;font-size:12px;line-height:19px;color:var(--text)}
.service-card .btn{position:static;margin-top:18px;width:98px;height:32px}

/* specialize */
.specialize{position:absolute;left:0;top:1112px;width:1200px;height:306px;background:linear-gradient(180deg,#1c2a38,#18222d)}
.specialize h2{position:absolute;top:58px;width:1200px;text-align:center;font:700 42px "Montserrat",sans-serif;color:var(--white)}
.spec-item{position:absolute;top:127px;width:260px;text-align:center;color:var(--white);font:400 19px "Montserrat",sans-serif}
.spec-icon{width:84px;height:84px;margin:0 auto 18px;border:2px solid var(--white);border-radius:50%;display:flex;align-items:center;justify-content:center}

/* about */
.about-photo{position:absolute;border-radius:20px 0 20px 0}
.about-text{position:absolute;left:600px;top:1532px;width:500px}
.about-text h2{font:700 42px "Montserrat",sans-serif;color:var(--ink)}
.about-text p{margin-top:14px;font-size:12px;line-height:21px}
.about-text .btn{position:static;margin-top:14px;width:98px;height:32px}

/* roof types */
.roof-types{position:absolute;left:0;top:1845px;width:1200px;height:394px;background:var(--grey-band)}
.roof-types h2{position:absolute;top:58px;width:1200px;text-align:center;font:600 40px "Montserrat",sans-serif;color:var(--ink)}
.roof-type{position:absolute;top:126px;width:200px;text-align:center;font:500 17px "Montserrat",sans-serif;color:var(--ink)}
.roof-type .swatch{width:170px;height:170px;margin:0 auto 18px;border-radius:50%;border:6px solid var(--blue)}

/* projects */
.projects-head{position:absolute;left:93px;top:2290px}
.project{position:absolute;width:333px;height:245px}
.project-label{display:flex;align-items:center;justify-content:center;height:100%;font:500 25px "Montserrat",sans-serif;color:var(--white)}

/* estimate */
.estimate-title{position:absolute;top:2952px;width:1200px;text-align:center;font:700 41px "Montserrat",sans-serif;color:var(--ink)}
.estimate-sub{position:absolute;top:3005px;width:1200px;text-align:center;font:400 21px "Montserrat",sans-serif;letter-spacing:9px;color:var(--ink)}
.tab{position:absolute;top:3053px;width:249px;height:37px;border:1px solid #ddd;border-radius:20px;display:flex;align-items:center;justify-content:center;font:400 15px "Montserrat",sans-serif;color:var(--ink)}
.tab.active{background:var(--blue);border-color:var(--blue);color:var(--white)}
.step-label{position:absolute;left:93px;top:3118px;font:700 18px "Montserrat",sans-serif;color:var(--ink)}
.step-label span{color:var(--blue)}
.shingle{position:absolute;top:3153px;width:249px;height:344px;background:var(--grey-band);text-align:center}
.shingle .photo{height:191px}
.shingle .tier{margin-top:14px;font-size:10px;color:var(--muted)}
.shingle h4{margin-top:6px;font:500 16px "Montserrat",sans-serif;color:var(--ink)}
.shingle .price{margin-top:6px;font:700 16px "Montserrat",sans-serif;color:var(--ink)}
.shingle .price span{color:var(--blue)}
.shingle .btn{position:static;margin:10px auto 0;width:124px;height:30px;font-size:10px}

/* testimonials */
.clients{position:absolute;left:0;top:3550px;width:1200px;height:396px;background:linear-gradient(180deg,#1e6e9f,#1a6292)}
.clients h2{position:absolute;top:58px;width:1200px;text-align:center;font:700 40px "Montserrat",sans-serif;color:var(--white)}
.quote-box{position:absolute;left:96px;top:160px;width:1009px;height:196px;border:1.5px solid rgba(255,255,255,.7);border-radius:98px}
.quote-mark{position:absolute;left:577px;top:133px;width:46px;height:46px;border-radius:50%;background:var(--white);display:flex;align-items:center;justify-content:center;font:700 34px Georgia,serif;color:var(--blue-deep);line-height:1;padding-top:12px}
.quote-text{position:absolute;left:135px;top:200px;width:930px;text-align:center;font-size:12.5px;line-height:23px;color:var(--white)}
.quote-name{position:absolute;left:505px;top:312px;width:190px;text-align:center;background:#1c6797;font:500 18px "Montserrat",sans-serif;color:var(--white)}
.arrow{position:absolute;top:228px;width:26px;height:26px;background:rgba(255,255,255,.15);border:1px solid rgba(255,255,255,.5);color:var(--white);display:flex;align-items:center;justify-content:center;font-size:14px}

/* footer */
.site-footer{position:absolute;left:0;top:3946px;width:1200px;height:333px;background:var(--footer)}
.f-col{position:absolute;top:52px;color:#9aa0a6;font-size:11px}
.f-col h5{font:400 19px "Montserrat",sans-serif;color:var(--white);margin-bottom:14px}
.f-col li{list-style:none;line-height:27px}
.f-col .line{line-height:33px}
.follow{margin-top:8px;font:700 10px "Montserrat",sans-serif;color:var(--white)}
.socials{display:flex;gap:5px;margin-top:8px}
.socials i{width:21px;height:21px;border-radius:50%;background:var(--white)}
.field{position:absolute;background:var(--white);font-size:9px;color:#666;padding:6px 8px}
.site-footer .btn{left:1041px;top:206px;width:64px;height:28px;font-size:10px}
.copyright{position:absolute;top:270px;width:1200px;text-align:center;font-size:11px;color:#8a9097}
.copyright span{color:var(--blue)}
</style>
</head>
<body>

<header class="site-header">
  <div class="brand"><span class="brand-mark"></span>EVERGREEN ROOFING</div>
  <div class="call">&#9742; Call Us: <b>555-014-2290</b></div>
  <nav class="nav"><span class="active">Home</span><span>About Us</span><span>Services</span><span>Projects</span><span>Instant Estimate</span><span>Contact Us</span></nav>
</header>

<section class="hero" role="img" aria-label="Photo of a large grey two-storey house with new roof and garage at dusk">
  <div class="hero-kicker">BUILT RIGHT</div>
  <div class="hero-title">BUILT TO LAST</div>
  <div class="btn">GET AN INSTANT ESTIMATE</div>
  <div class="dots"><i></i><i></i><i></i></div>
</section>

<section>
  <div class="services-intro">
    <div class="sec-kicker">OUR</div>
    <div class="sec-title">SERVICES</div>
    <p>Sed ut perspiciatis unde omnis iste natus error sit voluptatem accusantium doloremque laudantium, totam rem aperiam, eaque ipsa quae ab illo inventore veritatis et quasi architecto beatae vitae dicta sunt explicabo.</p>
  </div>
  <div class="service-card" style="left:440px">
    <div class="photo" role="img" aria-label="Photo of a roofer laying new roof panels under a blue sky" style="background:linear-gradient(160deg,#8fb4d6,#6a6f78 55%,#3d3f44)"></div>
    <h3>Roof Installation</h3>
    <p>Sed ut perspiciatis unde omnis iste natus error sit voluptatem accusantium doloremque laudantium, totam rem aperiam</p>
    <div class="btn">Read More</div>
  </div>
  <div class="service-card" style="left:778px">
    <div class="photo" role="img" aria-label="Photo of a worker repairing roof shingles at sunset" style="background:linear-gradient(160deg,#c98a5a,#7b7c84 50%,#474a52)"></div>
    <h3>Roof Repair</h3>
    <p>Sed ut perspiciatis unde omnis iste natus error sit voluptatem accusantium doloremque laudantium, totam rem aperiam</p>
    <div class="btn">Read More</div>
  </div>
</section>

<section class="specialize">
  <h2>WE SPECIALIZE</h2>
  <div class="spec-item" style="left:89px"><div class="spec-icon"><svg width="46" height="40" viewBox="0 0 46 40" fill="none" stroke="#fff" stroke-width="3"><rect x="3" y="5" width="40" height="30"/><line x1="23" y1="5" x2="23" y2="35"/><line x1="3" y1="20" x2="43" y2="20"/></svg></div>Windows/Skylights</div>
  <div class="spec-item" style="left:344px"><div class="spec-icon"><svg width="44" height="44" viewBox="0 0 44 44" fill="none" stroke="#fff" stroke-width="3"><path d="M4 8h36v6H4z"/><path d="M22 14v14l-6 10"/><circle cx="30" cy="34" r="3" fill="#fff"/></svg></div>Gutters</div>
  <div class="spec-item" style="left:596px"><div class="spec-icon"><svg width="44" height="40" viewBox="0 0 44 40" fill="none" stroke="#fff" stroke-width="3"><rect x="4" y="4" width="28" height="22"/><rect x="12" y="12" width="28" height="22" fill="#1b2632"/></svg></div>Siding</div>
  <div class="spec-item" style="left:851px"><div class="spec-icon"><svg width="44" height="42" viewBox="0 0 44 42" fill="#fff"><path d="M22 4l14 10H8z"/><path d="M22 16c3 4 4 6 4 8a4 4 0 0 1-8 0c0-2 1-4 4-8z"/><rect x="6" y="32" width="32" height="6"/></svg></div>Interior leak damage repairs</div>
</section>

<section>
  <div class="about-photo" role="img" aria-label="Photo of roofers working on a dark tiled roof" style="left:93px;top:1471px;width:236px;height:321px;background:linear-gradient(170deg,#4d86c8,#3a4a66 55%,#6b4a34)"></div>
  <div class="about-photo" role="img" aria-label="Photo of a roofer on a ladder against a tiled roof" style="left:336px;top:1501px;width:236px;height:291px;background:linear-gradient(170deg,#8ab8e6,#3e4e6a 55%,#2b3445)"></div>
  <div class="about-text">
    <h2>ABOUT US</h2>
    <p>After over a decade of general contracting, we continue to see a repetitive trend by the roof purchase process where homeowners are constantly left confused, nervous, and worried when they need a new roof. As one of the most important features of keeping your home safe, this is unacceptable. Evergreen Roofing was created to break this trend.</p>
    <div class="btn">Read More</div>
  </div>
</section>

<section class="roof-types">
  <h2>TYPES OF ROOFS</h2>
  <div class="roof-type" style="left:119px"><div class="swatch" role="img" aria-label="Close-up photo of cedar shingles" style="background:linear-gradient(135deg,#6d737c,#3d434b)"></div>CEDA</div>
  <div class="roof-type" style="left:374px"><div class="swatch" role="img" aria-label="Close-up photo of metal roofing" style="background:linear-gradient(135deg,#8a8e94,#50545a)"></div>METAL</div>
  <div class="roof-type" style="left:626px"><div class="swatch" role="img" aria-label="Close-up photo of slate tiles" style="background:linear-gradient(135deg,#5d6a7a,#35404d)"></div>SLATE</div>
  <div class="roof-type" style="left:881px"><div class="swatch" role="img" aria-label="Close-up photo of asphalt shingles" style="background:linear-gradient(135deg,#6f7f95,#3f4b5c)"></div>ASPHALT</div>
</section>

<section>
  <div class="projects-head"><div class="sec-kicker">RECENT</div><div class="sec-title">PROJECTS</div></div>
  <div class="project" role="img" aria-label="Project photo of a house in Lexington" style="left:93px;top:2385px;background:linear-gradient(160deg,#2c3036,#16191d)"><div class="project-label">Lexington, MA</div></div>
  <div class="project" role="img" aria-label="Aerial photo of a grey house among trees" style="left:433px;top:2385px;background:linear-gradient(160deg,#4f6a46,#7f8b92 55%,#4c5054)"></div>
  <div class="project" role="img" aria-label="Aerial photo of a large white house with driveway" style="left:773px;top:2385px;background:linear-gradient(160deg,#4a6a40,#c7cdd3 55%,#5d6166)"></div>
  <div class="project" role="img" aria-label="Photo of a curved shingle roof detail" style="left:93px;top:2638px;background:linear-gradient(160deg,#6a5e55,#a99781 55%,#d8d0c5)"></div>
  <div class="project" role="img" aria-label="Photo of a company truck parked beside a house" style="left:433px;top:2638px;background:linear-gradient(160deg,#dfe4ea,#9aa3ad 55%,#1b1d21)"></div>
  <div class="project" role="img" aria-label="Photo of a colonial house with lawn" style="left:773px;top:2638px;background:linear-gradient(180deg,#7ea7d8,#c4cdd2 50%,#5e7a45)"></div>
</section>

<section>
  <div class="estimate-title">INSTANT ESTIMATE</div>
  <div class="estimate-sub">CHOOSE YOUR ROOF TYPE</div>
  <div class="tab active" style="left:93px">1. Product Selection</div>
  <div class="tab" style="left:349px">2. About Your Roof</div>
  <div class="tab" style="left:605px">3. Roof Condition</div>
  <div class="tab" style="left:859px">4. Get Your Cost</div>
  <div class="step-label"><span>STEP 1:</span> PICK YOUR BRAND &amp; SHINGLE:</div>
  <div class="shingle" style="left:93px"><div class="photo" role="img" aria-label="Photo of grey shingle sample" style="background:linear-gradient(135deg,#7a8799,#3f4a5a)"></div><div class="tier">GOOD</div><h4>Finibus Bonorum Malorum</h4><div class="price"><span>$</span>214</div><div class="btn">Calculate Your Cost</div></div>
  <div class="shingle" style="left:349px"><div class="photo" role="img" aria-label="Photo of dark shingle sample" style="background:linear-gradient(135deg,#6a6e74,#34383d)"></div><div class="tier">BETTER</div><h4>Finibus Bonorum Malorum</h4><div class="price"><span>$</span>214</div><div class="btn">Calculate Your Cost</div></div>
  <div class="shingle" style="left:605px"><div class="photo" role="img" aria-label="Photo of slate shingle sample" style="background:linear-gradient(135deg,#5f6b7b,#323b47)"></div><div class="tier">BEST</div><h4>Finibus Bonorum Malorum</h4><div class="price"><span>$</span>214</div><div class="btn">Calculate Your Cost</div></div>
  <div class="shingle" style="left:859px"><div class="photo" role="img" aria-label="Photo of layered shingle sample" style="background:linear-gradient(135deg,#8c9098,#4a4e55)"></div><div class="tier">GOOD</div><h4>Finibus Bonorum Malorum</h4><div class="price"><span>$</span>214</div><div class="btn">Calculate Your Cost</div></div>
</section>

<section class="clients">
  <h2>HAPPY CLIENTS</h2>
  <div class="quote-box"></div>
  <div class="quote-mark">&ldquo;</div>
  <p class="quote-text">We needed to put a new roof on our house, as well as repair a sagging porch roof. Shingles had been flying off and we had had several leaks. Sam provided a very reasonable estimate - well below some of the other Home Pro Directory companies. The work was done very promptly and professionally. A couple of issues that arose were settled to our satisfaction and Sam took full ownership of the situation. It was very clear that customer satisfaction is a priority for this company. I would definitely recommend and hire again</p>
  <div class="quote-name">Dana Whitfield, MA</div>
  <div class="arrow" style="left:50px">&#8249;</div>
  <div class="arrow" style="left:1124px">&#8250;</div>
</section>

<footer class="site-footer">
  <div class="f-col" style="left:93px"><h5>Quick Links</h5><ul><li>Home</li><li>About Us</li><li>Services</li><li>Projects</li><li>Instant Estimate</li><li>Contact Us</li></ul></div>
  <div class="f-col" style="left:274px"><h5>Services</h5><ul><li>Roof Installation</li><li>Roof Repair</li><li>Windows/Skylights</li><li>Gutters</li><li>Siding</li><li>Interior leak damage repairs</li></ul></div>
  <div class="f-col" style="left:492px"><h5>Contact Us</h5><div class="line">48 Alder Lane, Northfield MA 01360</div><div class="line">555-014-2290</div><div class="line">info@evergreenroofingco.com</div><div class="follow">FOLLOW US</div><div class="socials"><i></i><i></i><i></i><i></i></div></div>
  <div class="f-col" style="left:751px"><h5>Quick Contact</h5></div>
  <div class="field" style="left:751px;top:87px;width:175px;height:30px">Name:</div>
  <div class="field" style="left:751px;top:121px;width:175px;height:30px">Email:</div>
  <div class="field" style="left:751px;top:155px;width:175px;height:30px">Phone:</div>
  <div class="field" style="left:932px;top:87px;width:173px;height:98px">Message:</div>
  <div class="btn">SUBMIT</div>
  <div class="copyright">COPYRIGHT © 2020 <span>EVERGREEN ROOFING</span>. ALL RIGHTS RESERVED.</div>
</footer>

</body>
</html>
```